Teach English in China Website Redesign Needed

We recruit native English speakers from the US, UK, etc. who want to teach English as a foreign language in schools in China. Our target customer is college educated, age 22-28 and they love to travel. We prefer designs with bright colors and lots of photos. We want to keep all the text on our current homepage, BrightPathTutors.com. We are open to changing our logo. A competitor's page that we like is bluekitemeadow.com because of their bright colors, photos and use of white space. We are happy to give you a dofollow link and design credit on our homepage. The use of included photos is optional. We need at least a home page design and a standard blog post design.
Target Market(s)
Our target customer is college educated, age 22-28 and they love to travel. Half of our customers are kindergarten teachers. Half of our customers are male.
Logo Text
Bright Path Tutors
Number of Pages Required
Requirements
Must have
- Bright colors
Should not have
- Our homepage must not look crowded. Use white space effectively.

```html
<!DOCTYPE html>
<html lang="en">
<head>
<meta charset="utf-8">
<title>Bright Path Tutors – Teach English in China</title>
<link href="https://fonts.googleapis.com/css2?family=Open+Sans:wght@400;600;700&family=Montserrat:wght@400;600;700&display=swap" rel="stylesheet">
<style>
:root{
  --red:#e0161f;
  --red-dark:#c8121a;
  --yellow:#f6b819;
  --green:#8cc63f;
  --ink:#222;
  --text:#666;
  --muted:#999;
  --light:#ededed;
  --dark:#2c2c2c;
  --footer:#2a2a2a;
  --white:#fff;
}
*{box-sizing:border-box;margin:0;padding:0}
html,body{width:1200px;height:4128px;overflow:hidden}
body{font-family:"Open Sans",Arial,sans-serif;color:var(--text);background:var(--white);position:relative}
.abs{position:absolute}
.photo{position:absolute}

/* header */
.site-header{position:absolute;left:0;top:0;width:1200px;height:110px;background:var(--white)}
.brand{position:absolute;left:118px;top:30px;display:flex;align-items:center;gap:12px}
.brand-mark{width:26px;height:26px;background:var(--red)}
.brand-name{font-family:"Montserrat",sans-serif;font-weight:700;font-size:26px;color:var(--ink);letter-spacing:.5px}
.social{position:absolute;left:925px;top:28px;display:flex;gap:8px}
.social span{width:22px;height:22px;border-radius:50%;background:#111;display:block}
.main-nav{position:absolute;right:118px;top:68px;display:flex;gap:42px;font-size:13px;color:#444;letter-spacing:.5px}
.main-nav a{color:inherit;text-decoration:none;padding-bottom:9px}
.main-nav a.active{border-bottom:2px solid var(--red)}

/* hero */
.hero{position:absolute;top:110px;left:0;width:1200px;height:501px;background:var(--light)}
.hero-photo{left:116px;top:17px;width:969px;height:473px;background:linear-gradient(120deg,#5d5b57 0%,#8d8a82 35%,#b7b3a9 60%,#3f4c44 100%)}
.hero-label{position:absolute;left:690px;top:240px;background:rgba(30,30,30,.8);color:var(--white);font-size:25px;padding:12px 24px;letter-spacing:.5px;border-bottom:3px solid var(--red)}

/* intro */
.intro{position:absolute;top:611px;left:0;width:1200px;height:498px;text-align:center}
.section-title{font-size:32px;color:var(--ink);font-weight:400;letter-spacing:1px}
.title-rule{width:40px;height:3px;background:var(--red);margin:12px auto 0}
.intro .section-title{margin-top:74px}
.intro-text{width:870px;margin:24px auto 0;font-size:13px;line-height:26px;color:#777}
.feature-cards{position:absolute;left:179px;top:297px;display:flex;gap:18px}
.feature-card{position:relative;width:264px;height:146px;padding:18px 22px;color:var(--white);text-align:left;overflow:hidden}
.feature-card h3{font-size:21px;font-weight:700;margin-bottom:8px}
.feature-card p{font-size:11.5px;line-height:17px;width:190px}
.card-red{background:var(--red)}
.card-yellow{background:var(--yellow)}
.card-green{background:var(--green)}
.feature-card svg{position:absolute;right:14px;bottom:10px;opacity:.35}

/* highlights */
.highlights{position:absolute;top:1109px;left:0;width:1200px;height:410px;background:var(--dark)}
.hl-accent{left:113px;top:58px;width:257px;height:320px;background:var(--red)}
.hl-photo{left:113px;top:88px;width:330px;height:250px;background:linear-gradient(135deg,#d9d4c8 0%,#b43c38 40%,#e5e0d4 70%,#8a7d6f 100%)}
.highlights .section-title{position:absolute;left:470px;top:54px;color:var(--white);font-size:30px;letter-spacing:2px}
.hl-rule{position:absolute;left:470px;top:98px;width:40px;height:3px;background:var(--red)}
.hl-list{position:absolute;left:470px;top:112px;list-style:none;width:640px}
.hl-list li{font-size:13px;line-height:17px;color:#eee;padding-left:20px;position:relative;margin-bottom:7px}
.hl-list li::before{content:"";position:absolute;left:0;top:5px;width:7px;height:7px;background:var(--white)}

/* testimonials */
.testimonials{position:absolute;top:1519px;left:0;width:1200px;height:440px;text-align:center}
.testimonials .section-title{margin-top:94px}
.section-sub{font-size:14px;color:var(--red);margin-top:16px}
.testimonial{position:absolute;top:242px;width:470px;height:160px}
.t-one{left:130px}
.t-two{left:637px}
.t-avatar{position:absolute;left:0;top:0;width:82px;height:82px}
.t-avatar-a{background:linear-gradient(135deg,#e7ddd2,#8a7a68)}
.t-avatar-b{background:#dcdcdc}
.t-name{position:absolute;left:-10px;top:92px;width:104px;font-size:14px;font-weight:700;color:var(--ink)}
.t-role{position:absolute;left:-20px;top:114px;width:124px;font-size:11px;color:var(--muted);font-style:italic}
.t-quote{position:absolute;left:140px;top:6px;width:290px;font-size:12px;line-height:19px;color:#555;text-align:center}
.t-mark{font-family:Georgia,serif;font-size:28px;color:#333;line-height:0;vertical-align:-8px}

/* faq */
.faq{position:absolute;top:1959px;left:0;width:1200px;height:477px}
.faq-panel{position:absolute;left:0;top:0;width:589px;height:477px;background:var(--red-dark);padding:38px 0 0 116px;color:var(--white)}
.faq-panel h2{font-size:40px;font-weight:600;letter-spacing:1px}
.faq-panel .lead{font-size:13px;margin-top:6px;margin-bottom:20px}
.faq-item{width:440px;border:1px solid rgba(255,255,255,.75);margin-bottom:12px;padding:11px 14px;font-size:13px;font-weight:600;position:relative}
.faq-item::after{content:"";position:absolute;right:16px;top:17px;border-left:4px solid var(--white);border-top:4px solid transparent;border-bottom:4px solid transparent}
.faq-item.open::after{transform:rotate(90deg)}
.faq-item p{font-weight:400;font-size:12.5px;line-height:20px;margin-top:10px}
.faq-photo{left:589px;top:0;width:611px;height:477px;background:linear-gradient(120deg,#c8c2ba 0%,#e8e3dc 30%,#7e8b82 60%,#c53a34 85%,#efefef 100%)}

/* blog */
.blog{position:absolute;top:2436px;left:0;width:1200px;height:729px;text-align:center}
.blog .section-title{margin-top:78px;font-size:38px}
.blog .section-sub{color:#888;margin-top:10px}
.blog-divider{position:absolute;left:300px;top:174px;width:600px;height:14px}
.blog-cards{position:absolute;left:157px;top:247px;display:flex;gap:22px;text-align:left}
.post-card{width:270px;height:350px;border:1px solid #e4e4e4;position:relative;background:var(--white)}
.post-img{height:166px}
.post-img-a{background:linear-gradient(135deg,#7d8a7a,#c03b36 50%,#d8d2c8)}
.post-img-b{background:linear-gradient(135deg,#e0d8ca,#c1463f 55%,#8b7d70)}
.post-img-c{background:linear-gradient(135deg,#5b4d48,#d5a18f 50%,#3d3533)}
.post-tag{position:absolute;right:14px;top:176px;background:var(--red);color:var(--white);font-size:9px;padding:2px 6px}
.post-title{font-size:14px;color:var(--ink);margin:30px 16px 0}
.post-excerpt{font-size:11px;line-height:16px;color:#888;margin:22px 16px 0}
.post-meta{position:absolute;left:0;bottom:0;width:100%;height:40px;border-top:1px solid #eee;font-size:10px;color:var(--muted);display:flex;align-items:center;padding:0 16px;gap:18px}
.post-meta .share{margin-left:auto}
.slider-dots{position:absolute;left:544px;top:632px;display:flex;gap:9px}
.slider-dots span{width:12px;height:12px;border-radius:50%;border:1px solid #bbb}
.slider-dots span.on{background:var(--red);border-color:var(--red)}

/* apply */
.apply{position:absolute;top:3165px;left:0;width:1200px;height:536px}
.apply-photo{left:0;top:0;width:1200px;height:536px;background:linear-gradient(110deg,#9ba6a2 0%,#d8d2c4 25%,#b84a40 55%,#6f7470 80%,#4a4b48 100%)}
.apply-panel{position:absolute;left:179px;top:63px;width:804px;height:432px;background:rgba(35,35,35,.85);padding:28px 28px 0;color:var(--white)}
.apply-panel h2{font-size:30px;font-weight:700}
.apply-panel .lead{font-size:13px;margin-top:4px}
.form-grid{display:grid;grid-template-columns:repeat(3,230px);gap:15px 28px;margin-top:24px}
.field{height:32px;background:var(--white);font-size:11px;color:#777;padding:0 8px;display:flex;align-items:center}
.field-message{grid-column:1 / 4;height:66px;align-items:flex-start;padding-top:8px}
.upload{position:absolute;left:28px;top:335px;font-size:12px;width:560px}
.file-btn{display:inline-block;margin-top:8px;background:var(--white);color:#333;font-size:10px;padding:2px 6px;border:1px solid #999}
.send-btn{position:absolute;left:611px;top:340px;width:162px;height:38px;background:var(--red);color:var(--white);font-size:13px;font-weight:700;display:flex;align-items:center;justify-content:center}

/* footer */
.site-footer{position:absolute;top:3701px;left:0;width:1200px;height:427px;background:var(--footer);color:#8a8a8a}
.f-col{position:absolute;top:80px}
.f-col h4{font-family:"Montserrat",sans-serif;font-size:14px;color:var(--white);font-weight:600}
.f-col .rule{width:30px;height:2px;background:var(--red);margin:9px 0 18px}
.f-col p{font-size:11.5px;line-height:18px;margin-bottom:12px;width:200px}
.f-links{display:grid;grid-template-columns:100px 110px;gap:8px 0;font-size:11.5px;color:#ccc}
.course{display:flex;gap:12px;margin-bottom:20px}
.course-thumb{width:52px;height:48px;background:#555}
.course-thumb.tint{background:#333c46}
.course strong{display:block;font-size:12px;color:var(--white)}
.course span{font-size:10px;line-height:15px}
.f-input{width:214px;height:34px;border:1px solid #444;font-size:11px;padding:0 8px;display:flex;align-items:center;margin-bottom:10px}
.f-textarea{height:70px;align-items:flex-start;padding-top:10px;position:relative}
.f-go{position:absolute;right:-1px;bottom:-1px;width:30px;height:22px;background:var(--red)}
.copyright{position:absolute;left:0;bottom:18px;width:100%;text-align:center;font-size:11px;border-top:1px solid #3a3a3a;padding-top:14px}
</style>
</head>
<body>

<header class="site-header">
  <div class="brand"><span class="brand-mark"></span><span class="brand-name">Bright Path Tutors</span></div>
  <div class="social"><span></span><span></span><span></span><span></span><span></span></div>
  <nav class="main-nav">
    <a class="active">HOME</a><a>AVAILABLE JOBS</a><a>APPLY ONLINE</a><a>BLOG</a><a>FAQ</a><a>CONTACT</a>
  </nav>
</header>

<section class="hero">
  <div class="photo hero-photo" role="img" aria-label="Teacher writing on a chalkboard in front of a classroom of Chinese students"></div>
  <div class="hero-label">TEACH ENGLISH IN CHINA</div>
</section>

<section class="intro">
  <h1 class="section-title">TEACH ENGLISH IN CHINA</h1>
  <div class="title-rule"></div>
  <p class="intro-text">Want to teach English in China? Do you enjoy teaching children or adults? Would you like the adventure of teaching in China for a year? Then we have the perfect job for you! We are seeking English speakers from the US, UK, Canada, Ireland, Australia, New Zealand and South Africa to teach English in China for a year (or longer if you wish). We recruit for hundreds of schools all over China such as Maple Bridge English, Summit Row English, Cedar Hill English, Lakeside English, Sunny Lane Kids, Willow Grove Kids, Red Lantern Academy, public schools, international schools, universities, and more.</p>
  <div class="feature-cards">
    <div class="feature-card card-red">
      <h3>Available Job</h3>
      <p>Lorem Ipsum is simply dummy text of the typesetting when an unknown printer scrambled.</p>
      <svg width="46" height="46" viewBox="0 0 46 46" fill="none" stroke="#fff" stroke-width="3"><circle cx="19" cy="19" r="13"/><line x1="28" y1="28" x2="42" y2="42"/></svg>
    </div>
    <div class="feature-card card-yellow">
      <h3>Required</h3>
      <p>Lorem Ipsum is simply dummy text of the typesetting when an unknown printer scrambled.</p>
      <svg width="46" height="46" viewBox="0 0 46 46" fill="none" stroke="#fff" stroke-width="3"><rect x="4" y="8" width="30" height="34"/><line x1="20" y1="30" x2="42" y2="6"/></svg>
    </div>
    <div class="feature-card card-green">
      <h3>We Offer</h3>
      <p>Lorem Ipsum is simply dummy text of the typesetting when an unknown printer scrambled.</p>
      <svg width="46" height="46" viewBox="0 0 46 46" fill="none" stroke="#fff" stroke-width="3"><rect x="8" y="4" width="30" height="38"/><line x1="14" y1="14" x2="32" y2="14"/><line x1="14" y1="22" x2="32" y2="22"/><line x1="14" y1="30" x2="32" y2="30"/></svg>
    </div>
  </div>
</section>

<section class="highlights">
  <div class="photo hl-accent"></div>
  <div class="photo hl-photo" role="img" aria-label="Young students in red uniforms working at desks in a classroom"></div>
  <h2 class="section-title">HIGHLIGHTS</h2>
  <div class="hl-rule"></div>
  <ul class="hl-list">
    <li>Competitive compensation: 7000-9000 RMB/month, up to 18,000 RMB (divide by 6.5 for US dollars) if you have a bachelor's degree, 2+ years of teaching experience</li>
    <li>Housing allowance: 2000 RMB/month (housing is cheaper in China)</li>
    <li>Teach private English lessons after work for 250 RMB/hr ($38 US per hour)</li>
    <li>Airfare reimbursement: 5000 RMB at end of completed 1 year contract</li>
    <li>Free TESOL / TEFL training and certification</li>
    <li>Invitation letter so you can apply for a visa (Z visa if you have a bachelor's degree).</li>
    <li>Airport pickup</li>
    <li>5-day work week, 25 hours teaching per week plus some office hours</li>
    <li>20 paid holidays</li>
    <li>Free Chinese classes 2 hours per week with most jobs</li>
  </ul>
</section>

<section class="testimonials">
  <h2 class="section-title">WHAT OUR USERS ARE SAYING</h2>
  <p class="section-sub">Find out why our users keep using Harbor Lane Exchange</p>
  <div class="testimonial t-one">
    <div class="photo t-avatar t-avatar-a" role="img" aria-label="Portrait photo of a reviewer"></div>
    <div class="t-name">John Doe</div>
    <div class="t-role">CEO - Company Name</div>
    <p class="t-quote"><span class="t-mark">“</span>The services Testimonials provides are marvelous. The support is fast and helpful. This Testimonial Slider helps increase customers and provide them safety and more information about your product through existing users.<span class="t-mark">”</span></p>
  </div>
  <div class="testimonial t-two">
    <div class="photo t-avatar t-avatar-b" role="img" aria-label="Placeholder portrait of a reviewer"></div>
    <div class="t-name">Samir Kadri</div>
    <div class="t-role">Dev - Brightwork Studio</div>
    <p class="t-quote"><span class="t-mark">“</span>The services Testimonials provides are marvelous. The support is fast and helpful. This Testimonial Slider helps increase customers and provide them safety and more information about your product through existing users.<span class="t-mark">”</span></p>
  </div>
</section>

<section class="faq">
  <div class="faq-panel">
    <h2>FAQ</h2>
    <p class="lead">Read frequently asked questions about our program.</p>
    <div class="faq-item">I can't speak Chinese. Is that a problem?</div>
    <div class="faq-item">Where in China do you place teachers and in what schools?</div>
    <div class="faq-item open">What's the next step after my Video Call interview?
      <p>We take excellent care of our teachers. Though we are paid by the schools we send teachers to, our number one priority is our teachers. We know what different schools are looking for and can quickly match you up with a school that will appreciate what you have to offer.</p>
    </div>
    <div class="faq-item">Will I have enough money to support myself?</div>
  </div>
  <div class="photo faq-photo" role="img" aria-label="Group of schoolchildren in uniforms with red scarves"></div>
</section>

<section class="blog">
  <h2 class="section-title">Blog Posts</h2>
  <p class="section-sub">Check out popular activities and hobby classes</p>
  <svg class="blog-divider" viewBox="0 0 600 14"><line x1="0" y1="2" x2="285" y2="2" stroke="#e2e2e2"/><polyline points="285,2 300,12 315,2" fill="none" stroke="#e2e2e2"/><line x1="315" y1="2" x2="600" y2="2" stroke="#e2e2e2"/></svg>
  <div class="blog-cards">
    <article class="post-card">
      <div class="post-img post-img-a" role="img" aria-label="Rows of students in uniform at a school assembly"></div>
      <span class="post-tag">New</span>
      <h3 class="post-title">Internet Entrepreneurship</h3>
      <p class="post-excerpt">Lorem ipsum dolor sit amet, consectetur adipisicing elit, sed do eiusmod tempor incididunt ut labore et dolore magna aliqua.</p>
      <div class="post-meta"><span>3 lessons</span><span>Beginner</span><span class="share">&lt;</span></div>
    </article>
    <article class="post-card">
      <div class="post-img post-img-b" role="img" aria-label="Children doing a painting activity in class"></div>
      <span class="post-tag">New</span>
      <h3 class="post-title">DIY: Stencil Painting on Bag</h3>
      <p class="post-excerpt">Lorem ipsum dolor sit amet, consectetur adipisicing elit, sed do eiusmod tempor incididunt ut labore et dolore magna aliqua.</p>
      <div class="post-meta"><span>Advanced</span><span class="share">&lt;</span></div>
    </article>
    <article class="post-card">
      <div class="post-img post-img-c" role="img" aria-label="Child with colourful face paint"></div>
      <span class="post-tag">New</span>
      <h3 class="post-title">Kids and Healthy Eating habits</h3>
      <p class="post-excerpt">Lorem ipsum dolor sit amet, consectetur adipisicing elit, sed do eiusmod tempor incididunt ut labore et dolore magna aliqua.</p>
      <div class="post-meta"><span>2 lessons</span><span>Intermediate</span><span class="share">&lt;</span></div>
    </article>
  </div>
  <div class="slider-dots"><span class="on"></span><span></span><span></span><span></span></div>
</section>

<section class="apply">
  <div class="photo apply-photo" role="img" aria-label="Bright classroom with students and red lanterns, softly blurred"></div>
  <div class="apply-panel">
    <h2>Apply Now</h2>
    <p class="lead">Fill out our short form and upload your resume.</p>
    <div class="form-grid">
      <div class="field">Your First and Last Name</div>
      <div class="field">Your Email</div>
      <div class="field">The time zone you're in</div>
      <div class="field">Phone</div>
      <div class="field">Video Call ID</div>
      <div class="field">Do you have a criminal history?</div>
      <div class="field">Your Birthdate</div>
      <div class="field">Do you have a 4-year degree?</div>
      <div class="field">start teaching in China?</div>
      <div class="field field-message">Message</div>
    </div>
    <div class="upload">Upload your CV / resume here or email it asap to mina@brightpathtutors.com. Choose File<br><span class="file-btn">Choose File</span></div>
    <div class="send-btn">SEND</div>
  </div>
</section>

<footer class="site-footer">
  <div class="f-col" style="left:118px">
    <h4>About StudyLeaf</h4><div class="rule"></div>
    <p>Lorem ipsum dolor sit amet, consectetur adipiscing elit, sed diam nonummy nibh euismod tincidunt.</p>
    <p>Morbi quis ante ornare, rhoncus lorem efficitur erat. Morbi est mi.</p>
  </div>
  <div class="f-col" style="left:361px">
    <h4>Quick Links</h4><div class="rule"></div>
    <div class="f-links">
      <span>Courses</span><span>Become Instructor</span>
      <span style="color:#fff">About Us</span><span>Terms of Use</span>
      <span>Events</span><span>Privacy Policy</span>
      <span>Blog</span><span>Legal Disclaimer</span>
      <span>Shortcodes</span><span></span>
    </div>
  </div>
  <div class="f-col" style="left:603px">
    <h4>Recent Courses</h4><div class="rule"></div>
    <div class="course"><div class="course-thumb"></div><div><strong>Web Theme Framework</strong><span>Short guide for new team<br>members, week one</span></div></div>
    <div class="course"><div class="course-thumb tint"></div><div><strong>Layout Kit 3 Updates</strong><span>Quick notes on what changed<br>this month</span></div></div>
  </div>
  <div class="f-col" style="left:845px">
    <h4>Quick Contact</h4><div class="rule"></div>
    <div class="f-input">Your email address</div>
    <div class="f-input f-textarea">Type your message<span class="f-go"></span></div>
  </div>
  <div class="copyright">Copyright 2017 Bright Path Tutors. All Rights Reserved</div>
</footer>

</body>
</html>
```